Homebuilder & Remodeling Firm looking for archectrual looking website

We are a Custom home building & remodeling company since 1986 and would like to launch a website.Carl Tondevik the principle of the firm is a graduate of Harwell Univesity school of architecture and draws his own designs and working drawings. and has done many residential, single and multi family projects in the Dallas Ft Worth Metroplex. We want our website to be architectural in design and visually appealing. We will eventually have photos to provide for you. The message we want to communicate is we have current update knowledge with trends, and longevity in experience. Our message is that we are a firm that designs and remodels fully through and we provide a well executed custom home that is unique to each client. The Homes that we build are unique ,authentic and sustainable architectural styles such as mid century modern, contemporary, transitional and they are sophisticated homes to compliment individual lifestyles of our clients. We have a passion for construction and an attention to detail that makes your dreams come to life. We listen to each clients every need in functionality and form and take them from pre-construction to post-construction follow -up.
We help you invest in your home. Thoughts Create Reality

EXAMPLES OF WEBSITES THAT WE LIKE. PLEASE DO
MORE CONTEMPORARY, SLEEK, ARCHITECTURAL

* Please make the LOGO a bigger part of design

http://pellamcrew.build/
https://www.vintrasol.co/
http://dostavanehomes.com/
http://www.milesfardowdesign.com/
http://www.quillmerton.com/
http://fennikdesignstudios.com/about
http://brandelorgc.com/

thank you,

Reason: We have many clients asking to see our website and re ready to launch something for them to look at

Target Market(s)

Home owners, home buyers, interior designers, All ages

Industry/Entity Type

Builders

Coding

Coded - Design and coding required

Number of Pages Required

5+ page

Font styles to use
Sans Serif

Requirements
Must have
• HTML5 OR PHP
• graphic artist must speak English:
• *Visually appealing, user friendly,
• * the website should reflect the stability and integrity of the company since it has been in business for over 30 years
• * a sophistication and refinement is our mandate.
Should not have
• Too busy, too much going on, we want more minimal in design and artsitic

```html
<!DOCTYPE html>
<html lang="en">
<head>
<meta charset="utf-8">
<title>Tondevik Development — Custom Homes &amp; Remodeling</title>
<link href="https://fonts.googleapis.com/css2?family=Poppins:wght@400;500;600&display=swap" rel="stylesheet">
<style>
  :root {
    --ink: #1d1d1f;
    --navy: #253a6b;
    --muted: #8a8a8a;
    --accent: #b6cc1a;
    --rule: #e2e2e2;
    --rule-dark: #8c8c8c;
    --white: #ffffff;
  }
  * { margin: 0; padding: 0; box-sizing: border-box; }
  html, body { width: 1200px; height: 794px; overflow: hidden; background: var(--white); }
  body { position: relative; font-family: "Poppins", sans-serif; color: var(--ink); }

  .brand { position: absolute; display: flex; align-items: center; gap: 7px; }
  .brand-mark { width: 22px; height: 26px; background: var(--navy); }
  .brand-text { display: flex; flex-direction: column; }
  .brand-name { font-size: 11.5px; font-weight: 500; color: var(--navy); letter-spacing: 0.1px; line-height: 1.1; }
  .brand-tagline { font-size: 4.8px; letter-spacing: 1.6px; color: var(--muted); margin-top: 2px; }
  .site-header .brand { left: 38px; top: 12px; }

  .call { position: absolute; left: 628px; top: 25px; font-size: 9px; font-weight: 500; letter-spacing: 0.3px; }
  .call .label { color: var(--muted); }
  .call .number { color: var(--ink); font-size: 10px; }
  .header-divider { position: absolute; left: 811px; top: 18px; width: 1px; height: 27px; background: var(--rule); }

  .social { position: absolute; display: flex; gap: 19px; }
  .social span { width: 9px; height: 9px; border-radius: 50%; background: var(--ink); display: block; }
  .social span:first-child { background: var(--accent); }
  .site-header .social { left: 846px; top: 27px; }

  .menu { position: absolute; left: 1113px; top: 26px; display: flex; align-items: center; gap: 12px; font-size: 9px; font-weight: 600; letter-spacing: 0.4px; }
  .menu svg { display: block; }

  .projects { position: absolute; top: 62px; left: 38px; width: 1124px; height: 428px; }
  .project { position: absolute; top: 0; height: 428px; overflow: hidden; }
  .project-photo { position: absolute; inset: 0; }
  .project-1 { left: 0; width: 428px; }
  .project-1 .project-photo { background: linear-gradient(180deg, #f3f3f3 0%, #c9cbcc 35%, #5a5a5a 62%, #1c1c1c 100%); }
  .project-2 { left: 446px; width: 428px; }
  .project-2 .project-photo { background: linear-gradient(180deg, #6b5649 0%, #8c7766 40%, #7a7767 65%, #3f4438 100%); }
  .project-3 { left: 893px; width: 231px; }
  .project-3 .project-photo { background: linear-gradient(180deg, #8f979c 0%, #a9afb0 35%, #5b6258 65%, #3c4a33 100%); }

  .project-title { position: absolute; left: 32px; top: 316px; color: var(--white); font-size: 20px; font-weight: 600; line-height: 22.5px; letter-spacing: -0.6px; }
  .project-link { position: absolute; left: 32px; top: 399px; color: var(--white); font-size: 9.5px; font-weight: 500; display: flex; align-items: center; gap: 8px; }

  .slider-arrow { position: absolute; top: 257px; }
  .slider-arrow.prev { left: 70px; }
  .slider-arrow.next { left: 1107px; }

  .progress { position: absolute; left: 38px; top: 549px; width: 1124px; height: 1px; background: var(--rule); }
  .progress-fill { position: absolute; left: 0; top: -1px; width: 146px; height: 2px; background: var(--rule-dark); }

  .site-footer .brand { left: 38px; top: 641px; }
  .footer-col { position: absolute; top: 642px; font-size: 9.5px; line-height: 15px; list-style: none; }
  .copyright { left: 234px; }
  .links-legal { left: 484px; }
  .links-legal li:first-child { color: var(--accent); }
  .links-company { left: 734px; }
  .language { position: absolute; left: 917px; top: 642px; font-size: 9.5px; display: flex; align-items: center; gap: 7px; }
  .site-footer .social { left: 1030px; top: 643px; }
</style>
</head>
<body>
  <header class="site-header">
    <div class="brand">
      <span class="brand-mark"></span>
      <span class="brand-text">
        <span class="brand-name">Tondevik Development</span>
        <span class="brand-tagline">CUSTOM HOMES • REMODELING</span>
      </span>
    </div>
    <div class="call"><span class="label">CALL US:</span> <span class="number">(+080) 5120 47 36 218</span></div>
    <div class="header-divider"></div>
    <nav class="social" aria-label="Social links"><span></span><span></span><span></span><span></span><span></span></nav>
    <div class="menu">MENU
      <svg width="12" height="10" viewBox="0 0 12 10"><path d="M0 1h12M0 5h12M0 9h12" stroke="#1d1d1f" stroke-width="1"/></svg>
    </div>
  </header>

  <main>
    <section class="projects">
      <article class="project project-1">
        <div class="project-photo" role="img" aria-label="Angular white concrete house on a still mountain lake"></div>
        <h2 class="project-title">Triangle<br>Concrete House<br>On Lake</h2>
        <a class="project-link">See project <svg width="5" height="9" viewBox="0 0 5 9"><path d="M.5.5l4 4-4 4" fill="none" stroke="#fff"/></svg></a>
      </article>
      <article class="project project-2">
        <div class="project-photo" role="img" aria-label="Textured museum building with glass bay over a reflecting pool"></div>
        <h2 class="project-title">Cubic<br>Inter Mesuem<br>In Rome</h2>
        <a class="project-link">See project <svg width="5" height="9" viewBox="0 0 5 9"><path d="M.5.5l4 4-4 4" fill="none" stroke="#fff"/></svg></a>
      </article>
      <article class="project project-3">
        <div class="project-photo" role="img" aria-label="Small pitched-roof house with timber screens and garden"></div>
        <h2 class="project-title">Small<br>House Near<br>Wroclaw</h2>
        <a class="project-link">See project <svg width="5" height="9" viewBox="0 0 5 9"><path d="M.5.5l4 4-4 4" fill="none" stroke="#fff"/></svg></a>
      </article>
    </section>
    <svg class="slider-arrow prev" width="20" height="36" viewBox="0 0 20 36" aria-label="Previous"><path d="M19 1L2 18l17 17" fill="none" stroke="#fff" stroke-width="1.4"/></svg>
    <svg class="slider-arrow next" width="20" height="36" viewBox="0 0 20 36" aria-label="Next"><path d="M1 1l17 17L1 35" fill="none" stroke="#fff" stroke-width="1.4"/></svg>
    <div class="progress"><div class="progress-fill"></div></div>
  </main>

  <footer class="site-footer">
    <div class="brand">
      <span class="brand-mark"></span>
      <span class="brand-text">
        <span class="brand-name">Tondevik Development</span>
        <span class="brand-tagline">CUSTOM HOMES • REMODELING</span>
      </span>
    </div>
    <ul class="footer-col copyright"><li>© Vintrasol 2017</li><li>All Rights Resevered</li></ul>
    <ul class="footer-col links-legal"><li>Site Map</li><li>Term &amp; Conditions</li><li>Privacy Policy</li><li>Help</li><li>Affiliate</li></ul>
    <ul class="footer-col links-company"><li>Our Location</li><li>Career</li><li>About</li><li>Contact</li></ul>
    <div class="language">English <svg width="9" height="5" viewBox="0 0 9 5"><path d="M.5.5l4 4 4-4" fill="none" stroke="#8a8a8a"/></svg></div>
    <nav class="social" aria-label="Social links"><span></span><span></span><span></span><span></span><span></span></nav>
  </footer>
</body>
</html>
```